Boutique custom software development company needs new business card

Our nearly 20 year old custom software development company would like to better include the fact that we are now providing Bitcoin services. These new services are B2B include education (how to acquire and securely hold Bitcoin) and integrating Bitcoin payments into existing ecommerce sites or other existing systems. Please keep the card clean and simple. Attached is our current design and some other files. vexalon.example

Target Market(s)

businesses owners interested in long term relationship

Industry/Entity Type

Custom software development and Bitcoin

Contact Information for Business Card

Marcus Ellwood, marcus@vexalon.example, vexalon.example, (888) 555-VEXAL

Font styles to use
Other font styles liked:
• monospace

Requirements
Must have
• double-sided
Nice to have
• clean and simple
Should not have
• physical address

```html
<!DOCTYPE html>
<html lang="en">
<head>
<meta charset="utf-8">
<title>Vexalon Business Card</title>
<link href="https://fonts.googleapis.com/css2?family=Montserrat:wght@400;500;700;800&display=swap" rel="stylesheet">
<style>
  :root {
    --backdrop: #4f4f4f;
    --card: #f1f0ee;
    --ink: #2b2b2b;
    --blue: #4f83bb;
    --orange: #e68c45;
  }
  * { margin: 0; padding: 0; box-sizing: border-box; }
  html, body {
    width: 1200px; height: 900px; overflow: hidden;
    background: var(--backdrop);
    font-family: "Montserrat", sans-serif;
  }
  .stage {
    position: relative; width: 1200px; height: 900px;
    display: flex; align-items: center; justify-content: center; gap: 50px;
  }
  .card {
    position: relative; width: 525px; height: 300px;
    background: var(--card); overflow: hidden;
    box-shadow: 0 12px 30px rgba(0,0,0,0.35);
  }
  .card-accents { position: absolute; inset: 0; width: 100%; height: 100%; }

  /* front */
  .front-brand {
    position: absolute; left: 0; right: 0; top: 104px; text-align: center;
  }
  .brand-name {
    font-weight: 800; font-size: 58px; letter-spacing: 1px; line-height: 1;
    color: var(--blue);
  }
  .brand-tagline {
    margin-top: 6px; font-weight: 400; font-size: 19px; color: var(--blue);
    letter-spacing: -0.2px;
  }

  /* back */
  .back-mark {
    position: absolute; left: 62px; top: 70px; width: 118px; text-align: center;
  }
  .mark-square {
    width: 96px; height: 96px; margin: 0 auto; background: var(--blue);
  }
  .mark-site {
    margin-top: 10px; font-size: 15px; font-weight: 500; color: var(--ink);
  }
  .contact {
    position: absolute; right: 34px; top: 44px; text-align: right; color: var(--ink);
  }
  .contact-name {
    display: inline-block; font-size: 24px; letter-spacing: 0.5px;
  }
  .contact-name .given { font-weight: 800; }
  .contact-name .family {
    font-weight: 400; border-bottom: 2px solid var(--blue); padding-bottom: 2px;
  }
  .contact-line {
    display: flex; align-items: center; justify-content: flex-end; gap: 10px;
    margin-top: 16px; font-size: 16px; font-weight: 500; letter-spacing: 0.4px;
  }
  .contact-line:first-of-type { margin-top: 26px; }
  .contact-icon {
    width: 18px; height: 18px; background: var(--blue); border-radius: 3px;
    display: flex; align-items: center; justify-content: center;
  }
</style>
</head>
<body>
<main class="stage">

  <section class="card card-front" aria-label="Card front">
    <svg class="card-accents" viewBox="0 0 525 300" aria-hidden="true">
      <polygon points="0,188 42,180 98,268 88,300 0,300" fill="var(--orange)"/>
      <polygon points="525,0 525,96 486,104 420,24 442,0" fill="var(--blue)"/>
    </svg>
    <div class="front-brand">
      <div class="brand-name">VEXALON</div>
      <div class="brand-tagline">developer of custom applications</div>
    </div>
  </section>

  <section class="card card-back" aria-label="Card back">
    <svg class="card-accents" viewBox="0 0 525 300" aria-hidden="true">
      <polygon points="0,272 300,272 322,262 525,262 525,300 0,300" fill="var(--orange)"/>
      <polygon points="300,272 322,262 525,262 525,300 340,300" fill="var(--blue)"/>
      <polygon points="0,280 525,280 525,300 0,300" fill="var(--orange)"/>
      <polygon points="318,280 525,262 525,300 330,300" fill="var(--blue)"/>
    </svg>
    <div class="back-mark">
      <div class="mark-square"></div>
      <div class="mark-site">vexalon.example</div>
    </div>
    <div class="contact">
      <div class="contact-name"><span class="given">MARCUS</span> <span class="family">ELLWOOD</span></div>
      <div class="contact-line">
        <span>(888) 555-VEXAL</span>
        <span class="contact-icon">
          <svg width="12" height="12" viewBox="0 0 24 24" aria-hidden="true"><path fill="#fff" d="M6.6 10.8a15.1 15.1 0 0 0 6.6 6.6l2.2-2.2c.3-.3.7-.4 1-.2 1.1.4 2.3.6 3.6.6.6 0 1 .4 1 1V20c0 .6-.4 1-1 1A17 17 0 0 1 3 4c0-.6.4-1 1-1h3.5c.6 0 1 .4 1 1 0 1.3.2 2.5.6 3.6.1.3 0 .7-.2 1z"/></svg>
        </span>
      </div>
      <div class="contact-line">
        <span>marcus@vexalon.example</span>
        <span class="contact-icon">
          <svg width="12" height="12" viewBox="0 0 24 24" aria-hidden="true"><rect x="2" y="5" width="20" height="14" fill="none" stroke="#fff" stroke-width="2"/><path d="M2 5l10 8 10-8" fill="none" stroke="#fff" stroke-width="2"/></svg>
        </span>
      </div>
    </div>
  </section>

</main>
</body>
</html>
```